I need a business card for myself, being a proprietor of a funeral parlor based in Manila. I'd like the card to have either of the following:
White Font on Black Background
or
Black Font on White Background
No logo is needed however I will appreciate any efforts to show a symbol of eternal happiness, aptly designed with above mentioned colors in mind.
Company name, address and contact on the lower right corner.
Logo or symbol anywhere.
Quillstone Funeral Services
+639174826351
darvik4521@pelmora.com
corner of Brisco Avenue and Velhurst Street
Makati City, Philippines
Thank you.
Update: Please include a small dove in your design. You are free to choose where you would like it on the card.

```html
<!DOCTYPE html>
<html lang="en">
<head>
<meta charset="utf-8">
<title>Quillstone Funeral Services – Business Card</title>
<link href="https://fonts.googleapis.com/css2?family=Roboto+Condensed:wght@400;700&display=swap" rel="stylesheet">
<style>
  :root {
    --paper: #ffffff;
    --card-dark: #231f20;
    --card-glow: #4d4a4b;
    --ink-light: #ffffff;
    --ink-dark: #1e1b1c;
    --trim-red: #e0242b;
    --crop-mark: #231f20;
    --spray-light: rgba(255, 255, 255, 0.16);
    --spray-soft: rgba(255, 255, 255, 0.05);
  }
  * { margin: 0; padding: 0; box-sizing: border-box; }
  html, body {
    width: 1200px; height: 872px; overflow: hidden;
    background: var(--paper);
    font-family: "Roboto Condensed", "Arial Narrow", sans-serif;
  }
  .sheet { position: relative; width: 1200px; height: 872px; }
  .crop-marks { position: absolute; inset: 0; }
  .business-card {
    position: absolute; left: 341px; top: 273px;
    width: 517px; height: 326px;
    background: radial-gradient(ellipse 190px 140px at 50% 32%, var(--card-glow), var(--card-dark) 100%);
    border: 1px solid var(--trim-red);
    color: var(--ink-light);
    overflow: hidden;
  }
  .upper-panel {
    position: absolute; left: 0; top: 0; width: 100%; height: 190px;
    display: flex; align-items: center; justify-content: center; gap: 18px;
    padding-top: 14px;
  }
  .floral-spray {
    width: 128px; height: 120px;
    border-radius: 10px;
  }
  .floral-spray--left {
    background: linear-gradient(135deg, var(--spray-soft) 0%, var(--spray-light) 55%, var(--spray-soft) 100%);
  }
  .floral-spray--right {
    background: linear-gradient(225deg, var(--spray-soft) 0%, var(--spray-light) 55%, var(--spray-soft) 100%);
  }
  .brand-mark {
    width: 112px; text-align: center;
    font-weight: 700; font-size: 24px; line-height: 1;
    color: var(--ink-light);
  }
  .name-band {
    position: absolute; left: 0; top: 190px; width: 100%; height: 33px;
    background: var(--ink-light);
    display: flex; align-items: center; justify-content: center;
  }
  .company-name {
    color: var(--ink-dark); font-weight: 700; font-size: 26px; line-height: 1;
  }
  .contact-line {
    position: absolute; left: 0; width: 100%;
    display: flex; justify-content: center; align-items: center; gap: 26px;
    font-size: 15px; line-height: 1;
  }
  .contact-line--address { top: 246px; }
  .contact-line--reach { top: 277px; }
  .contact-item { display: flex; align-items: center; gap: 3px; }
  .contact-icon { width: 13px; height: 13px; flex: none; }
</style>
</head>
<body>
<div class="sheet">
  <svg class="crop-marks" width="1200" height="872" aria-hidden="true">
    <g stroke="var(--crop-mark)" stroke-width="1">
      <line x1="357" y1="257" x2="357" y2="273"/>
      <line x1="841" y1="257" x2="841" y2="273"/>
      <line x1="324" y1="289" x2="341" y2="289"/>
      <line x1="858" y1="289" x2="875" y2="289"/>
      <line x1="324" y1="583" x2="341" y2="583"/>
      <line x1="858" y1="583" x2="875" y2="583"/>
      <line x1="357" y1="599" x2="357" y2="615"/>
      <line x1="841" y1="599" x2="841" y2="615"/>
    </g>
  </svg>

  <div class="business-card">
    <div class="upper-panel">
      <div class="floral-spray floral-spray--left" role="img" aria-label="White line-drawn floral spray of leaves and blossoms curving toward the centre"></div>
      <div class="brand-mark">Quillstone</div>
      <div class="floral-spray floral-spray--right" role="img" aria-label="Mirrored white line-drawn floral spray of leaves and blossoms"></div>
    </div>

    <div class="name-band">
      <h1 class="company-name">Quillstone Funeral Services</h1>
    </div>

    <div class="contact-line contact-line--address">
      <span class="contact-item">
        <svg class="contact-icon" viewBox="0 0 14 14" aria-hidden="true">
          <circle cx="7" cy="7" r="6" fill="none" stroke="currentColor" stroke-width="1"/>
          <path d="M7 10.5 L4.6 6.6 A2.6 2.6 0 1 1 9.4 6.6 Z" fill="currentColor"/>
          <circle cx="7" cy="5.6" r="0.9" fill="var(--card-dark)"/>
        </svg>
        <span>: Corner of Brisco Avenue and Velhurst Street, Makati City, Philippines</span>
      </span>
    </div>

    <div class="contact-line contact-line--reach">
      <span class="contact-item">
        <svg class="contact-icon" viewBox="0 0 14 14" aria-hidden="true">
          <circle cx="7" cy="7" r="6" fill="none" stroke="currentColor" stroke-width="1"/>
          <path d="M4.5 3.8 L5.8 3.6 L6.5 5.4 L5.6 6.1 Q6.4 7.8 8 8.5 L8.7 7.6 L10.4 8.3 L10.2 9.6 Q9.6 10.4 8.6 10.2 Q4.3 9 3.8 5 Q3.8 4.2 4.5 3.8 Z" fill="currentColor"/>
        </svg>
        <span>: +639174826351</span>
      </span>
      <span class="contact-item">
        <svg class="contact-icon" viewBox="0 0 14 14" aria-hidden="true">
          <circle cx="7" cy="7" r="6" fill="none" stroke="currentColor" stroke-width="1"/>
          <rect x="3.8" y="4.8" width="6.4" height="4.4" fill="none" stroke="currentColor" stroke-width="0.9"/>
          <path d="M3.8 4.8 L7 7.4 L10.2 4.8" fill="none" stroke="currentColor" stroke-width="0.9"/>
        </svg>
        <span>: darvik4521@pelmora.com</span>
      </span>
    </div>
  </div>
</div>
</body>
</html>
```